Wordpress Theme Design for Glacé-Ember

Hi, I am looking for an awesome WORDPRESS theme for my snoball and coffee business that is called Glacé-Ember. This has to be a wordpress theme, because I have other plugins that I would like to use with this site. I want the design to be professional and sophisticated, but also appeal to kids, because after all, the main focus of the business is going to be snoballs, which kids love. I don't want it to look too much like a kiddy site, though. I am also going to be selling other items such as frito pies, hotdogs, cotton candy, nachos, pickles, candy, toys, etc, but the main focus will be the hot and cold aspect of the coffee and snoballs (hence the name, "Glacé-Ember"). I want the design to look very creative/original and really be attractive to kids, but also very professional so that even adults like coming to the site.
Somewhere in the design I would like to be able to advertise other local businesses in the future, so I would like space incorporated into the design for that. I would also like to be able to add other pages if I want, so there should be space along the top for links, such as "home", "contact", etc. It would also be nice to have a footer in the design for links or other plugins. If you take a look at the site http://wobblypupclipsz.example/, I like the functionality of the site (for example, the layout, links, footer, sidebar on other pages), but obviously there isn't much custom design with the theme.
I actually already have a logo designed that I would like incorporated into the look and feel of the design, so that should give you a good place to start with your design. I want the graphics in the theme to really be eye-catching. You are more than welcome to tweak my current logo, blend it into the theme, whatever...(if you want half of the page to be frozen, and the other half to be fire-ish, doesn't have to be, just giving ideas...any and all designs I will take into consideration). Basically, whatever you think would look amazing.
The more amazing the design, I would definitely give a bonus for.
If this helps you out, I'm not looking for a "glossy" style of wordpress design. I really like how this site (ArtHiveNet) is made. It uses softer, cleaner colors and designs...it's kind of like a "grunge" style with its text and designs (what I mean is it's not a cookie cutter type of design), but nothing too extreme grunge by any means. I'm looking for the same style as the ArtHiveNet site, only with the flare of my type of business.
Hope this helps
Thank you
Updates
Reason: The designs, although nice, are not really what I am looking for. These all just feel like they are ready made templates, and I'm looking for something a little more original and unique.

```html
<!DOCTYPE html>
<html lang="en">
<head>
<meta charset="utf-8">
<title>Glacé-Ember — Snoballs and Coffee</title>
<link href="https://fonts.googleapis.com/css2?family=Ropa+Sans&family=PT+Sans:wght@400;700&display=swap" rel="stylesheet">
<style>
:root{
  --nav-top:#3bb6ee;
  --nav-bottom:#1a93d4;
  --blue-heading:#1b8cc4;
  --red-accent:#d8182a;
  --ink:#3a3a3a;
  --muted:#8a8a8a;
  --button-blue:#29aee6;
  --frame-grey:#dcdcdc;
  --footer-top:#222222;
  --footer-bottom:#121212;
  --footer-text:#e6e6e6;
  --footer-muted:#9a9a9a;
}
*{margin:0;padding:0;box-sizing:border-box}
h1,h2,h3,h4{font-weight:400}
html,body{width:758px;height:1200px;overflow:hidden;background:#fff}
body{font-family:"PT Sans",sans-serif;color:var(--ink)}
.page{position:relative;width:758px;height:1200px;overflow:hidden;background:#fff}
.abs{position:absolute}

/* navigation */
.main-nav{left:0;top:0;width:758px;height:48px;background:linear-gradient(var(--nav-top),var(--nav-bottom));display:flex;align-items:center;justify-content:space-between;padding:0 26px 0 29px;box-shadow:0 2px 3px rgba(0,0,0,.2)}
.main-nav a{font-family:"Ropa Sans",sans-serif;font-size:13px;color:#fff;text-decoration:none}

/* header */
.header-band{left:0;top:48px;width:758px;height:384px;background:radial-gradient(circle at 30% 40%,#f2f2f2,#dcdcdc 70%,#d2d2d2)}
.brand{left:34px;top:86px;display:flex;align-items:center;gap:6px;font-family:"Ropa Sans",sans-serif;font-size:24px;color:var(--red-accent)}
.brand-dot{width:16px;height:16px;border-radius:50%;background:var(--blue-heading)}
.social{top:103px;width:34px;height:34px;border-radius:50%;background:radial-gradient(circle at 40% 35%,#fafafa,#c9c9c9);box-shadow:0 1px 3px rgba(0,0,0,.35)}

/* slider */
.slider{left:20px;top:152px;width:716px;height:257px;background:#fff;border:1px solid #e2e2e2;box-shadow:0 3px 8px rgba(0,0,0,.15)}
.slide-photo-cup{left:22px;top:2px;width:340px;height:245px;background:radial-gradient(ellipse at 50% 55%,#8a4b2a,#c9a58c 45%,#f4f2f0 72%)}
.slide-photo-beans{left:545px;top:175px;width:170px;height:80px;background:linear-gradient(160deg,#fff 30%,#a7683f 65%,#5a2a12)}
.slide-title{left:368px;top:44px;font-family:"Ropa Sans",sans-serif;font-size:23px;color:var(--blue-heading);white-space:nowrap}
.slide-subtitle{left:368px;top:70px;font-family:"Ropa Sans",sans-serif;font-size:29px;color:var(--red-accent);white-space:nowrap}
.slide-text{left:370px;top:107px;width:290px;font-size:8.6px;line-height:13px;color:#444}
.order-button{left:368px;top:153px;width:95px;height:29px;border-radius:15px;background:linear-gradient(#eeeeee,#d6d6d6);font-family:"Ropa Sans",sans-serif;font-size:13px;color:#333;display:flex;align-items:center;justify-content:center}
.slide-arrow{top:112px;width:21px;height:30px;background:var(--red-accent);display:flex;align-items:center;justify-content:center}
.slide-arrow.prev{left:-1px;border-radius:0 4px 4px 0}
.slide-arrow.next{right:-1px;border-radius:4px 0 0 4px}

/* content */
.section-heading{font-family:"Ropa Sans",sans-serif;font-size:14.5px;color:var(--blue-heading);white-space:nowrap}
.body-copy{font-size:8.3px;line-height:14px;color:#444}
.body-copy p+p{margin-top:14px}
.video{left:500px;top:473px;width:238px;height:161px;background:radial-gradient(ellipse at 50% 80%,#2a140a,#6b3a1e 40%,#b58d72 70%,#d9c2b4)}
.play{left:101px;top:63px;width:34px;height:34px;border-radius:50%;background:rgba(230,230,230,.75);display:flex;align-items:center;justify-content:center}
.divider{left:22px;top:667px;width:715px;height:1px;background:#bdbdbd}
.feature-frame{top:716px;width:214px;height:88px;background:var(--frame-grey);padding:4px}
.feature-photo{width:100%;height:100%}
.feature-text{top:814px;width:214px;font-size:8.3px;line-height:14px;color:#444}
.read-more{top:863px;width:62px;height:19px;background:var(--button-blue);color:#fff;font-family:"Ropa Sans",sans-serif;font-size:10px;display:flex;align-items:center;justify-content:center;border-radius:2px}

/* footer */
.site-footer{left:0;top:917px;width:758px;height:283px;background:linear-gradient(var(--footer-top),var(--footer-bottom))}
.footer-heading{font-family:"Ropa Sans",sans-serif;font-size:14px;color:var(--footer-text);white-space:nowrap}
.footer-item{font-size:8.3px;line-height:13.5px;color:var(--footer-text)}
.footer-meta{font-size:8.8px;color:var(--footer-muted);margin-top:3px}
.footer-rule{border-top:1px dashed #555;margin:8px 0}
.thumb{width:70px;height:58px;border:2px solid #f2f2f2;border-radius:3px}
.footer-line{left:20px;top:1143px;width:718px;height:1px;background:#333}
.footer-links{left:0;top:1152px;width:758px;text-align:center;font-size:8.3px;color:#cfcfcf}
.footer-links span.sep{margin:0 4px;color:#888}
.copyright{left:0;top:1171px;width:758px;text-align:center;font-size:7.5px;color:#b5b5b5}
</style>
</head>
<body>
<div class="page">

  <nav class="main-nav abs">
    <a>Home</a><a>About Us</a><a>Our Coffee</a><a>Our Snoballs</a><a>Order now</a><a>Services</a><a>Blog</a><a>Testimonials</a><a>Contact Us</a>
  </nav>

  <div class="header-band abs" role="img" aria-label="Soft grey background with snowflake pattern"></div>

  <div class="brand abs"><span class="brand-dot"></span>Glacé-Ember</div>

  <span class="social abs" style="left:612px"></span>
  <span class="social abs" style="left:649px"></span>
  <span class="social abs" style="left:686px"></span>

  <section class="slider abs">
    <div class="slide-photo-cup abs" role="img" aria-label="Glass coffee cup filled with coffee beans on a saucer"></div>
    <div class="slide-photo-beans abs" role="img" aria-label="Scoop of roasted coffee beans"></div>
    <h2 class="slide-title abs">Need Best Snowballs and Coffee</h2>
    <h1 class="slide-subtitle abs">Come to Glacé-Ember</h1>
    <p class="slide-text abs">We at Pennyvale provide you the best simple websites too with total work done as using all the best designing and all done so that you can achieve the goal of yours through our work done on your website.</p>
    <div class="order-button abs">ORDER NOW</div>
    <div class="slide-arrow prev abs"><svg width="8" height="12" viewBox="0 0 8 12"><path d="M6 1 1 6l5 5" fill="none" stroke="#fff" stroke-width="2"/></svg></div>
    <div class="slide-arrow next abs"><svg width="8" height="12" viewBox="0 0 8 12"><path d="M2 1l5 5-5 5" fill="none" stroke="#fff" stroke-width="2"/></svg></div>
  </section>

  <h3 class="section-heading abs" style="left:22px;top:447px">Welcome to Glacé-Ember Website Mainpage</h3>
  <div class="body-copy abs" style="left:22px;top:469px;width:455px">
    <p>Pennyvale eSolutions is a web service company, offering a wide range of services which range from designing and development, that is covering almost all the fields in the best possible way. To be the best we know what and how to present beautifully the working of the client's need and their advantages be highlighted. We act in accordance with the Industry certified processes to deliver the best to our clients all over the world.</p>
    <p>Thus, Wanna get ahead in the competition with other websites…. Pennyvale esolutions provide you with an attractive and most convincing website to enhance your marketing goals.</p>
    <p>The only way to success is through the right path and that's what we provide you. None of the other companies has the result we do. So stick to the best that's how you will be the best don't opt for the second best. Our expertise does not limit itself to web development but also it includes Web Hosting, Search Engine Optimization, E-Commerce. We partner hundreds of organization to enhance their business, marketing and profit goals.</p>
  </div>

  <h3 class="section-heading abs" style="left:500px;top:447px">Our Video</h3>
  <div class="video abs" role="img" aria-label="Milk being poured into a cup of black coffee">
    <div class="play abs"><svg width="12" height="14" viewBox="0 0 12 14"><path d="M1 0l11 7-11 7z" fill="#333"/></svg></div>
  </div>

  <div class="divider abs"></div>

  <h3 class="section-heading abs" style="left:22px;top:693px">Snow &amp; Coffee Shop</h3>
  <div class="feature-frame abs" style="left:22px"><div class="feature-photo" role="img" aria-label="Cappuccino with heart-shaped cocoa art" style="background:linear-gradient(160deg,#f6f1ec,#c9a98d 55%,#7a5238)"></div></div>
  <p class="feature-text abs" style="left:22px">To be the best we know what and how to present beautifully the working of the client's need and their advantages be highlighted.</p>
  <div class="read-more abs" style="left:20px">read more...</div>

  <h3 class="section-heading abs" style="left:270px;top:693px">Our Features &amp; Services</h3>
  <div class="feature-frame abs" style="left:271px"><div class="feature-photo" role="img" aria-label="Coffee cups and marshmallows on a white table" style="background:linear-gradient(160deg,#f4efea,#d9c4b0 50%,#8f6a4c)"></div></div>
  <p class="feature-text abs" style="left:272px">To be the best we know what and how to present beautifully the working of the client's need and their advantages be highlighted.</p>
  <div class="read-more abs" style="left:272px">read more...</div>

  <h3 class="section-heading abs" style="left:519px;top:693px">Why Choouse Us?</h3>
  <div class="feature-frame abs" style="left:519px"><div class="feature-photo" role="img" aria-label="Two people chatting over coffee" style="background:linear-gradient(120deg,#6b4a36,#b08a6e 45%,#4a3326)"></div></div>
  <p class="feature-text abs" style="left:519px">To be the best we know what and how to present beautifully the working of the client's need and their advantages be highlighted.</p>
  <div class="read-more abs" style="left:519px">read more...</div>

  <footer class="site-footer abs"></footer>

  <h4 class="footer-heading abs" style="left:22px;top:941px">Recent Comments Blog</h4>
  <div class="abs" style="left:22px;top:968px;width:220px">
    <p class="footer-item">We act in accordance with the Industry certified processes to deliver the best to our clients all over the world.</p>
    <p class="footer-meta">By Author Name</p>
    <div class="footer-rule"></div>
    <p class="footer-item">The only way to success is through the right path and that's what we provide you. None of the other companies has the result we do. So stick to the best that's how you will be the best don't opt for the second best.</p>
    <p class="footer-meta">By Author Name</p>
  </div>

  <h4 class="footer-heading abs" style="left:282px;top:941px">Recent Posts</h4>
  <div class="abs" style="left:282px;top:962px;width:199px">
    <p class="footer-item">We here modify the site to improve the ranking by using the keywords and contents.</p>
    <p class="footer-meta">Posted on 20 March 2012 05:05 AM</p>
    <div class="footer-rule"></div>
    <p class="footer-item">Best Coffee &amp; Snow Services only here.</p>
    <p class="footer-meta">Posted on 18 March 2012 05:05 AM</p>
    <div class="footer-rule"></div>
    <p class="footer-item">We at Pennyvale provide you the best simple websites too with total work done as using</p>
    <p class="footer-meta">Posted on 18 March 2012 05:05 AM</p>
  </div>

  <h4 class="footer-heading abs" style="left:527px;top:941px">Have a look on Coffee &amp; Snow</h4>
  <div class="thumb abs" style="left:531px;top:967px;background:linear-gradient(150deg,#5a2e17,#a06a45 50%,#f1e8dc)" role="img" aria-label="Coffee cup among roasted beans"></div>
  <div class="thumb abs" style="left:615px;top:967px;background:linear-gradient(150deg,#f1e7de,#c89f7e 55%,#7c5236)" role="img" aria-label="Cappuccino with heart art"></div>
  <div class="thumb abs" style="left:531px;top:1036px;background:radial-gradient(circle at 45% 45%,#ffffff,#e8e4df 55%,#b9b0a6)" role="img" aria-label="White snowball treats"></div>
  <div class="thumb abs" style="left:615px;top:1036px;background:linear-gradient(150deg,#d9d6d2,#6c5446 55%,#2e221b)" role="img" aria-label="Sprinkled chocolate snowballs"></div>

  <div class="footer-line abs"></div>
  <div class="footer-links abs">Home<span class="sep">|</span>About Us<span class="sep">|</span>Our Coffee<span class="sep">|</span>Our Snoballs<span class="sep">|</span>Order now<span class="sep">|</span>Services<span class="sep">|</span>Blog<span class="sep">|</span>Testimonials<span class="sep">|</span>Contact Us</div>
  <div class="copyright abs">© 2012 Company Name &nbsp;|&nbsp; All right reserved &nbsp;|&nbsp; Term &amp; Condtions</div>

</div>
</body>
</html>
```